8 x 8 Social Media Design - Tax, Accounting & Bookkeeping Service

Bright Ledger Advisory Group, Inc.

Tax, Accounting and Bookkeeping Services

“We provide our services, with you next mortgage in mind”

Special pricing available for all Mortgage Loan Customers!!

President / CEO Marcus Delaney

Primary service provider with over 27 years of experience

Call directly for more information: (555) 284-9037

Or email at: mdelaney@brightledgerhq.example

```html
<!DOCTYPE html>
<html lang="en">
<head>
<meta charset="utf-8">
<title>Bright Ledger Advisory Group – Tax, Accounting and Bookkeeping Services</title>
<link rel="stylesheet" href="https://fonts.googleapis.com/css2?family=Playfair+Display:wght@500;700;800&family=Montserrat:wght@400;500;600;700&family=Oswald:wght@400;600&display=swap">
<style>
  :root {
    --blue-deep: #14307a;
    --blue-bright: #2a5cb8;
    --navy-dark: #071a36;
    --navy-light: #0f2f5e;
    --gold-dark: #b27a2a;
    --gold-mid: #d9b04c;
    --gold-light: #ecd577;
    --ink: #1c1c1c;
    --white: #ffffff;
    --badge-text: #b8732a;
  }
  * { margin: 0; padding: 0; box-sizing: border-box; }
  html, body { width: 1200px; height: 1200px; overflow: hidden; background: #ffffff; }
  .post { position: relative; width: 1200px; height: 1200px; overflow: hidden; background: var(--white); font-family: "Montserrat", sans-serif; }
  .backdrop { position: absolute; inset: 0; }
  .headline {
    position: absolute; left: 58px; top: 38px;
    font-family: "Playfair Display", serif; font-weight: 800;
    font-size: 96px; line-height: 100px; letter-spacing: -0.5px;
    background: linear-gradient(100deg, var(--blue-deep) 0%, var(--blue-bright) 45%, var(--blue-deep) 80%);
    -webkit-background-clip: text; background-clip: text; color: transparent;
  }
  .subline {
    position: absolute; left: 60px; top: 376px;
    font-size: 40px; line-height: 48px; font-weight: 400; color: var(--ink);
  }
  .experience {
    position: absolute; left: 60px; top: 822px;
    font-size: 31px; line-height: 39px; font-weight: 600; color: var(--ink); letter-spacing: 0.3px;
  }
  .company {
    position: absolute; left: 62px; top: 990px; width: 400px; text-align: center;
    font-family: "Playfair Display", serif; font-weight: 700; font-size: 38px; line-height: 46px;
    color: var(--gold-mid);
  }
  .contact { position: absolute; left: 520px; top: 935px; width: 660px; text-align: center; color: var(--white); }
  .contact-name {
    font-family: "Playfair Display", serif; font-weight: 500; font-size: 82px; line-height: 96px;
    color: var(--gold-mid); letter-spacing: 1px;
  }
  .contact-role { font-size: 24px; font-weight: 500; margin-top: 4px; }
  .contact-phone { font-size: 34px; font-weight: 700; margin-top: 18px; display: flex; align-items: center; justify-content: center; gap: 14px; }
  .contact-email { font-size: 29px; font-weight: 400; margin-top: 10px; display: flex; align-items: center; justify-content: center; gap: 14px; }
  .icon { flex: none; }
</style>
</head>
<body>
<main class="post">
  <svg class="backdrop" width="1200" height="1200" viewBox="0 0 1200 1200">
    <defs>
      <linearGradient id="gold" x1="0" y1="0" x2="1" y2="1">
        <stop offset="0" stop-color="var(--gold-dark)"/>
        <stop offset="0.45" stop-color="var(--gold-light)"/>
        <stop offset="1" stop-color="var(--gold-dark)"/>
      </linearGradient>
      <linearGradient id="gold-band" x1="0" y1="0" x2="1" y2="0">
        <stop offset="0" stop-color="var(--gold-dark)"/>
        <stop offset="0.6" stop-color="var(--gold-light)"/>
        <stop offset="1" stop-color="var(--gold-mid)"/>
      </linearGradient>
      <linearGradient id="navy" x1="0" y1="0" x2="1" y2="1">
        <stop offset="0" stop-color="var(--navy-dark)"/>
        <stop offset="0.55" stop-color="var(--navy-light)"/>
        <stop offset="1" stop-color="var(--navy-dark)"/>
      </linearGradient>
      <radialGradient id="seal" cx="0.4" cy="0.35" r="0.7">
        <stop offset="0" stop-color="#f6e07a"/>
        <stop offset="0.7" stop-color="#d9a532"/>
        <stop offset="1" stop-color="#a86d1c"/>
      </radialGradient>
      <linearGradient id="portrait" x1="0" y1="0" x2="0" y2="1">
        <stop offset="0" stop-color="#2a2c36"/>
        <stop offset="0.35" stop-color="#6b4a3a"/>
        <stop offset="0.6" stop-color="#1e2433"/>
        <stop offset="1" stop-color="#141a28"/>
      </linearGradient>
      <path id="badge-ring" d="M1002,251 A96,96 0 1 1 1098,251"/>
    </defs>

    <!-- photo band -->
    <rect x="0" y="553" width="820" height="257" fill="var(--white)"/>
    <g role="img" aria-label="Photo of three professionals reviewing documents at a meeting table">
      <rect x="0" y="557" width="372" height="241" fill="#8d8478"/>
    </g>
    <g role="img" aria-label="Photo of a joyful couple unpacking moving boxes in their new home">
      <rect x="386" y="557" width="420" height="241" fill="#b9a893"/>
    </g>

    <!-- gold sweep -->
    <path d="M1141,0 L1200,0 L1200,918 L0,918 L0,810 L683,810 C712,700 752,610 812,535 C890,440 980,340 1035,272 C1095,198 1128,90 1141,0 Z"
          fill="url(#gold)" stroke="var(--white)" stroke-width="8"/>
    <rect x="0" y="810" width="1200" height="108" fill="url(#gold-band)"/>

    <!-- portrait -->
    <g role="img" aria-label="Portrait of the company president in a dark hat, glasses and suit">
      <path d="M735,918 L735,560 C735,420 840,316 970,316 C1100,316 1200,400 1200,520 L1200,918 Z" fill="url(#portrait)"/>
    </g>

    <!-- navy footer -->
    <rect x="0" y="918" width="1200" height="282" fill="url(#navy)"/>
    <rect x="0" y="915" width="1200" height="4" fill="var(--gold-mid)"/>

    <!-- pricing badge -->
    <circle cx="1050" cy="168" r="116" fill="var(--white)"/>
    <circle cx="1050" cy="168" r="80" fill="url(#seal)" stroke="#a86d1c" stroke-width="3"/>
    <text font-family="Montserrat, sans-serif" font-weight="600" font-size="17" letter-spacing="3" fill="var(--badge-text)">
      <textPath href="#badge-ring">FOR ALL MORTGAGE LOAN CUSTOMERS</textPath>
    </text>
    <g font-family="Oswald, sans-serif" fill="var(--ink)" text-anchor="middle">
      <text x="1050" y="150" font-size="38" font-weight="600">SPECIAL</text>
      <text x="1050" y="186" font-size="38" font-weight="600">PRICING</text>
      <text x="1050" y="215" font-size="26" font-weight="400">AVAILABLE</text>
    </g>
  </svg>

  <h1 class="headline">Tax, Accounting<br>and Bookkeeping<br>Services</h1>
  <p class="subline">We provide our services,<br>with you next mortgage<br>in mind</p>
  <p class="experience">PRIMARY SERVICE PROVIDER WITH<br>OVER 27 YEARS OF EXPERIENCE</p>

  <p class="company">Bright Ledger<br>Advisory Group, Inc.</p>

  <section class="contact">
    <h2 class="contact-name">Marcus Delaney</h2>
    <p class="contact-role">President / CEO</p>
    <p class="contact-phone">
      <svg class="icon" width="22" height="28" viewBox="0 0 22 28"><path d="M6,2 L10,2 L11,8 L8,10 C9,15 11,19 14,21 L17,19 L21,23 L19,27 C10,27 3,17 3,6 Z" fill="var(--gold-mid)"/></svg>
      (555) 284-9037
    </p>
    <p class="contact-email">
      <svg class="icon" width="28" height="20" viewBox="0 0 28 20"><rect x="1" y="1" width="26" height="18" fill="var(--gold-mid)"/><path d="M1,1 L14,11 L27,1" fill="none" stroke="var(--navy-dark)" stroke-width="2"/></svg>
      mdelaney@brightledgerhq.example
    </p>
  </section>
</main>
</body>
</html>
```